NEED Homepage Website Design for Event Planning Business

We need a homepage mockup for an event planning company based in Massachusetts. We provide a custom trailer to rent along with chairs, tables, lighting, etc.

Please add a "Check Availability" call to action which is just a form
- First & Last Name
- Phone
- Email Address
- Date Request

Add an Snapshots section (use attached photos as we do not even have an IG account yet)

1 page

```html
<!DOCTYPE html>
<html lang="en">
<head>
<meta charset="utf-8">
<title>Full Circle Events — Event Planning & Trailer Rentals</title>
<link rel="stylesheet" href="https://fonts.googleapis.com/css2?family=Roboto+Slab:wght@300;400;500&family=Roboto:wght@400&display=swap">
<style>
:root{
  --ink:#2b2b2b;
  --muted:#555;
  --white:#ffffff;
  --mist:#f4f4f4;
  --dark:#141414;
  --pill:#222222;
  --hero-a:#3b4049;
  --hero-b:#23272e;
  --line:#3a3a3a;
}
*{box-sizing:border-box;margin:0;padding:0}
html,body{width:1200px;height:3657px;overflow:hidden}
body{font-family:"Roboto Slab",Georgia,serif;color:var(--ink);background:var(--white)}
.wrap{width:978px;margin:0 auto}
.rule{width:68px;height:3px;background:var(--ink);margin:18px auto 0}
.rule.light{background:var(--white)}
.section-title{font-weight:400;font-size:36px;text-align:center}

/* header */
.site-header{height:138px}
.site-header .wrap{display:flex;align-items:center;justify-content:space-between;height:138px}
.brand{display:flex;align-items:center;gap:12px;font-size:30px;font-weight:500;color:var(--ink);letter-spacing:.5px}
.brand-dot{width:20px;height:20px;border-radius:50%;background:var(--ink)}
.main-nav{display:flex;gap:39px;font-size:15px;font-family:"Roboto Slab",serif}
.main-nav a{color:var(--ink);text-decoration:none}

/* hero */
.hero{position:relative;height:697px;background:linear-gradient(180deg,#5b6068 0%,var(--hero-a) 40%,var(--hero-b) 100%);color:var(--white)}
.hero-panel{position:absolute;left:290px;top:195px;width:620px;height:320px;background:rgba(30,33,40,.45)}
.hero-copy{position:absolute;left:0;right:0;top:230px;text-align:center}
.hero-copy .kicker{font-size:44px;font-weight:400}
.hero-copy h1{font-size:72px;font-weight:400;line-height:1.1;margin-top:6px}
.btn-outline{display:inline-block;border:2px solid var(--white);border-radius:32px;color:var(--white);text-decoration:none;font-size:20px;padding:17px 38px}
.hero .btn-outline{margin-top:24px}

/* welcome */
.welcome{height:547px;padding-top:56px;text-align:center}
.welcome-copy{width:740px;margin:42px auto 0;font-size:14px;line-height:29px;color:var(--muted);font-weight:300}
.welcome-copy p+p{margin-top:29px}

/* services */
.services{height:652px;background:var(--mist);padding-top:38px}
.service-grid{display:flex;gap:12px;margin-top:40px}
.service-card{width:235px;height:366px;background:var(--white);box-shadow:0 1px 3px rgba(0,0,0,.08);text-align:center}
.service-photo{height:202px}
.service-card h3{font-weight:400;font-size:21px;margin-top:20px}
.service-card p{font-family:"Roboto",Arial,sans-serif;font-size:13.5px;line-height:26px;color:var(--muted);margin:12px 14px 0}
.center{text-align:center}
.btn-solid{display:inline-block;margin-top:38px;background:var(--pill);color:var(--white);text-decoration:none;border-radius:30px;font-size:16px;padding:17px 31px}

/* quote */
.quote{height:505px;background:linear-gradient(180deg,#3c4149,#262a31);color:var(--white);padding-top:62px}
.quote .section-title{color:var(--white)}
.quote-form{width:646px;margin:34px auto 0;display:grid;grid-template-columns:1fr 1fr;gap:14px 9px}
.quote-form label{display:block;height:48px;background:var(--white);border-radius:3px;color:var(--ink);font-size:15px;padding:15px 17px}
.quote-form .full{grid-column:1/3}
.quote .btn-outline{margin-top:38px;font-size:18px;padding:17px 35px}

/* gallery */
.feed{height:751px;padding-top:44px}
.feed-grid{display:grid;grid-template-columns:repeat(3,315px);gap:17px 16px;margin-top:40px}
.feed-tile{position:relative;height:256px}
.feed-badge{position:absolute;right:14px;bottom:14px;width:44px;height:44px;border-radius:50%;background:rgba(30,30,30,.75)}
.feed-badge::after{content:"";position:absolute;left:14px;top:14px;width:16px;height:16px;border:2px solid var(--white);border-radius:50%}

/* footer */
.site-footer{height:367px;background:var(--dark);color:var(--white);text-align:center;padding-top:46px}
.site-footer .brand{justify-content:center;color:var(--white);font-size:36px}
.site-footer .brand-dot{background:var(--white)}
.footer-nav{display:flex;justify-content:center;gap:41px;margin-top:56px;font-size:15px}
.footer-nav a{color:var(--white);text-decoration:none}
.social{display:flex;justify-content:center;gap:6px;margin-top:30px}
.social span{width:32px;height:32px;border:1.5px solid var(--white);border-radius:50%;display:flex;align-items:center;justify-content:center}
.social span::after{content:"";width:8px;height:8px;border-radius:50%;background:var(--white)}
.copyright{font-size:12px;margin-top:26px}
</style>
</head>
<body>

<header class="site-header">
  <div class="wrap">
    <div class="brand"><span class="brand-dot"></span>Full Circle Events</div>
    <nav class="main-nav">
      <a href="#">HOME</a><a href="#">ABOUT US</a><a href="#">SERVICES</a><a href="#">PRICING</a><a href="#">GALLERY</a><a href="#">CONTACT US</a>
    </nav>
  </div>
</header>

<section class="hero" role="img" aria-label="Event trailer with bar, umbrellas and barrel tables at dusk">
  <div class="hero-panel"></div>
  <div class="hero-copy">
    <div class="kicker">Full Circle</div>
    <h1>Events</h1>
    <a class="btn-outline" href="#">READ MORE</a>
  </div>
</section>

<section class="welcome">
  <h2 class="section-title">Welcome to FCE Events</h2>
  <div class="rule"></div>
  <div class="welcome-copy">
    <p>Welcome to Full-Circle-Events ! We provide everything you need to host any event desired!! Our goal is to provide an atmosphere that will blow away the competition and leave you feeling that you hosted an event which will leave everyone talking!!</p>
    <p>We are event planners who will provide all the goods and bring new ideas to the table that have never been done before! Starting with our main attraction the FCE event trailer which was just completed last summer! We typically start booking your event with the entertainment trailer and build off of that. What ever the occasion and whatever you desire, we will go beyond your expectations!</p>
    <p>Our Entertainment trailer includes a full service bar with a 4x8 storage room for everything your bartender needs to serve your guests. Around the bar we have 7- 30 inch stools and a U-shaped seating area on the back which includes 5 more stools for a friendly gathering area.</p>
  </div>
</section>

<section class="services">
  <h2 class="section-title">Our Services</h2>
  <div class="rule"></div>
  <div class="wrap">
    <div class="service-grid">
      <article class="service-card">
        <div class="service-photo" role="img" aria-label="Trailer set up with canopy and barrel tables" style="background:linear-gradient(180deg,#7d8a6a,#4a4f4c)"></div>
        <h3>Trailer For Events</h3>
        <p>Sed ut perspiciatis unde omnis iste natus error sit voluptatem acc usan tium doloremque</p>
      </article>
      <article class="service-card">
        <div class="service-photo" role="img" aria-label="Trailer bar with string lights and seating" style="background:linear-gradient(180deg,#8f9684,#3e403c)"></div>
        <h3>Table and Chair</h3>
        <p>Sed ut perspiciatis unde omnis iste natus error sit voluptatem acc usan tium doloremque</p>
      </article>
      <article class="service-card">
        <div class="service-photo" role="img" aria-label="Wood-panelled trailer beside a house" style="background:linear-gradient(180deg,#a7a9a2,#8a5f3a)"></div>
        <h3>Whisky barrel</h3>
        <p>Sed ut perspiciatis unde omnis iste natus error sit voluptatem acc usan tium doloremque</p>
      </article>
      <article class="service-card">
        <div class="service-photo" role="img" aria-label="Tent attached to trailer over tables" style="background:linear-gradient(180deg,#c9ccc9,#4f4c45)"></div>
        <h3>Tent setup</h3>
        <p>Sed ut perspiciatis unde omnis iste natus error sit voluptatem acc usan tium doloremque</p>
      </article>
    </div>
    <div class="center"><a class="btn-solid" href="#">View All Services</a></div>
  </div>
</section>

<section class="quote" role="img" aria-label="Dimmed backdrop of the event trailer and patio">
  <h2 class="section-title">Request A Quote</h2>
  <div class="rule light"></div>
  <form class="quote-form">
    <label>First Name :</label>
    <label>Last Name :</label>
    <label>Phone :</label>
    <label>Email :</label>
    <label class="full">Date Request :</label>
  </form>
  <div class="center"><a class="btn-outline" href="#">Check Availability</a></div>
</section>

<section class="feed">
  <h2 class="section-title">Follow Snapshots</h2>
  <div class="rule"></div>
  <div class="wrap">
    <div class="feed-grid">
      <div class="feed-tile" role="img" aria-label="Tent and trailer on a patio" style="background:linear-gradient(180deg,#c7cbc8,#3f3d38)"><span class="feed-badge"></span></div>
      <div class="feed-tile" role="img" aria-label="Barrel table under an umbrella with stools" style="background:linear-gradient(180deg,#4e4a55,#7a6a4c)"><span class="feed-badge"></span></div>
      <div class="feed-tile" role="img" aria-label="Indoor hall with round tables and sunflowers" style="background:linear-gradient(180deg,#5a5856,#b9b2a8)"><span class="feed-badge"></span></div>
      <div class="feed-tile" role="img" aria-label="White trailer bar with flowers and steps" style="background:linear-gradient(180deg,#dedcd6,#5c5a52)"><span class="feed-badge"></span></div>
      <div class="feed-tile" role="img" aria-label="Trailer in front of a grey house on a lawn" style="background:linear-gradient(180deg,#9aa0a6,#4f7a34)"><span class="feed-badge"></span></div>
      <div class="feed-tile" role="img" aria-label="Trailer parked among trees" style="background:linear-gradient(180deg,#6f8a5a,#8b7a62)"><span class="feed-badge"></span></div>
    </div>
  </div>
</section>

<footer class="site-footer">
  <div class="brand"><span class="brand-dot"></span>Full Circle Events</div>
  <nav class="footer-nav">
    <a href="#">HOME</a><a href="#">ABOUT US</a><a href="#">SERVICES</a><a href="#">PRICING</a><a href="#">GALLERY</a><a href="#">CONTACT US</a>
  </nav>
  <div class="social"><span></span><span></span><span></span><span></span><span></span></div>
  <p class="copyright">© Copyright 2021 FCE Events All Rights Reserved</p>
</footer>

</body>
</html>
```